Infographics breakdown for small group

An infographic is needed to display the different personality types from a spreadsheet for 18 individuals. Name of the organization: Cedar Harvest Fellowship Church Atlanta
Updates

Infographics of an Excel spreadsheet for 19 people at a church. The name of the church is Cedar Harvest Fellowship Chruch Atlanta.

Target Market(s)

Church group

Industry/Entity Type

Spirtual

Requirements
Must have
• Age, Personality, and Spiritual Gifts breakdown
Nice to have
• Compelling photo,
Should not have
• I'm okay with the designer deciding

```html
<!DOCTYPE html>
<html lang="en">
<head>
<meta charset="utf-8">
<title>Personality Type &amp; Top 5 Gifts – Cedar Harvest Fellowship Chruch</title>
<link rel="stylesheet" href="https://fonts.googleapis.com/css2?family=Libre+Baskerville:wght@700&family=Roboto+Slab:wght@600;800&family=Arimo:wght@400&display=swap">
<style>
:root{
  --sky:#bfdbf2;
  --navy:#2d2e74;
  --chip:#d9ebeb;
  --ink:#161616;
  --white:#ffffff;
}
*{margin:0;padding:0;box-sizing:border-box}
html,body{width:848px;height:1200px;overflow:hidden;background:var(--sky)}
.poster{position:relative;width:848px;height:1200px;background:var(--sky);overflow:hidden;font-family:"Arimo",Arial,sans-serif;color:var(--ink)}
.side-band{position:absolute;left:0;top:0;width:25px;height:1200px;background:var(--navy)}
.decor{position:absolute;left:0;top:0;width:848px;height:1200px;z-index:1}
.rule{position:absolute;height:1px;background:var(--ink);z-index:0}
.title{position:absolute;left:0;width:848px;top:52px;text-align:center;font-family:"Libre Baskerville",Georgia,serif;font-weight:700;font-size:38px;line-height:38px;letter-spacing:-1px;color:var(--ink);z-index:2}
.brand{position:absolute;left:894px;top:0;z-index:2}
.brand-mark{position:absolute;left:628px;top:266px;width:166px;height:166px;border:6px solid var(--white);border-radius:50%;z-index:2}
.brand-name{position:absolute;left:590px;width:244px;top:458px;text-align:center;color:var(--white);z-index:2}
.brand-name .org{font-family:"Libre Baskerville",Georgia,serif;font-weight:700;font-size:31px;line-height:38px;letter-spacing:-0.5px}
.brand-name .sub{font-family:"Arimo",Arial,sans-serif;font-size:17.5px;line-height:23px;margin-top:4px}
.icon-badge{position:absolute;left:655px;top:109px;width:80px;height:80px;border-radius:50%;background:#d8eaea;z-index:2}
.section{position:absolute;left:0;width:848px;z-index:2}
.type-info{position:absolute;left:54px;top:0;width:180px}
.type-name{font-family:"Roboto Slab",Georgia,serif;font-weight:800;font-size:18px;letter-spacing:1.6px;line-height:22px}
.type-code{font-size:13px;line-height:16px;margin-top:4px}
.type-desc{font-size:10.8px;line-height:13.6px;margin-top:7px}
.divider-v{position:absolute;left:240px;top:0;width:1px;background:var(--ink)}
.person{position:absolute}
.person-name{display:inline-block;background:var(--chip);padding:2px 8px 1px;font-family:"Roboto Slab",Georgia,serif;font-weight:600;font-size:13.6px;line-height:17px;white-space:nowrap}
.gifts{list-style:none;padding-left:8px;margin-top:13px;font-size:12.4px;line-height:15.7px;white-space:nowrap}
.c1{left:265px}.c2{left:415px}.c3{left:567px}.c4{left:691px}
</style>
</head>
<body>
<div class="poster">
  <div class="side-band"></div>

  <div class="rule" style="left:53px;top:303px;width:520px"></div>
  <div class="rule" style="left:53px;top:457px;width:500px"></div>
  <div class="rule" style="left:53px;top:612px;width:560px"></div>
  <div class="rule" style="left:53px;top:765px;width:752px"></div>
  <div class="rule" style="left:53px;top:1036px;width:752px"></div>

  <svg class="decor" viewBox="0 0 848 1200" aria-hidden="true">
    <circle cx="894" cy="430" r="348" fill="#2d2e74"/>
    <polygon points="576,703 607,684 601,726" fill="#d8eaea"/>
    <g fill="#2d2e74">
      <g transform="translate(47,52)">
        <circle cx="0" cy="0" r="2.2"/><circle cx="12" cy="0" r="2.2"/><circle cx="24" cy="0" r="2.2"/><circle cx="36" cy="0" r="2.2"/>
        <circle cx="0" cy="12" r="2.2"/><circle cx="12" cy="12" r="2.2"/><circle cx="24" cy="12" r="2.2"/><circle cx="36" cy="12" r="2.2"/>
        <circle cx="0" cy="24" r="2.2"/><circle cx="12" cy="24" r="2.2"/><circle cx="24" cy="24" r="2.2"/><circle cx="36" cy="24" r="2.2"/>
        <circle cx="0" cy="36" r="2.2"/><circle cx="12" cy="36" r="2.2"/><circle cx="24" cy="36" r="2.2"/><circle cx="36" cy="36" r="2.2"/>
      </g>
      <g transform="translate(528,204)">
        <circle cx="0" cy="0" r="2.2"/><circle cx="12" cy="0" r="2.2"/><circle cx="24" cy="0" r="2.2"/><circle cx="36" cy="0" r="2.2"/>
        <circle cx="0" cy="12" r="2.2"/><circle cx="12" cy="12" r="2.2"/><circle cx="24" cy="12" r="2.2"/><circle cx="36" cy="12" r="2.2"/>
        <circle cx="0" cy="24" r="2.2"/><circle cx="12" cy="24" r="2.2"/><circle cx="24" cy="24" r="2.2"/><circle cx="36" cy="24" r="2.2"/>
        <circle cx="0" cy="36" r="2.2"/><circle cx="12" cy="36" r="2.2"/><circle cx="24" cy="36" r="2.2"/><circle cx="36" cy="36" r="2.2"/>
      </g>
      <g transform="translate(51,955)">
        <circle cx="0" cy="0" r="2.2"/><circle cx="12" cy="0" r="2.2"/><circle cx="24" cy="0" r="2.2"/><circle cx="36" cy="0" r="2.2"/>
        <circle cx="0" cy="12" r="2.2"/><circle cx="12" cy="12" r="2.2"/><circle cx="24" cy="12" r="2.2"/><circle cx="36" cy="12" r="2.2"/>
        <circle cx="0" cy="24" r="2.2"/><circle cx="12" cy="24" r="2.2"/><circle cx="24" cy="24" r="2.2"/><circle cx="36" cy="24" r="2.2"/>
        <circle cx="0" cy="36" r="2.2"/><circle cx="12" cy="36" r="2.2"/><circle cx="24" cy="36" r="2.2"/><circle cx="36" cy="36" r="2.2"/>
      </g>
    </g>
  </svg>

  <h1 class="title">PERSONALITY TYPE<br>&amp; TOP 5 GIFTS</h1>

  <div class="icon-badge" role="img" aria-label="Small brain icon in a pale circle"></div>
  <div class="brand-mark"></div>
  <div class="brand-name">
    <div class="org">CEDAR<br>HARVEST</div>
    <div class="sub">Fellowship Chruch<br>Atlanta, Georgia</div>
  </div>

  <section class="section" style="top:174px">
    <div class="type-info">
      <h2 class="type-name">ADVENTURER</h2>
      <p class="type-code">ISFP-A/ISFP-T</p>
      <p class="type-desc">(Flexible and charming artists, always ready to explore and experience something new.)</p>
    </div>
    <div class="divider-v" style="height:113px;top:-4px"></div>
    <div class="person c1"><span class="person-name">Lena Whitaker</span>
      <ul class="gifts"><li>Craftsmanship,</li><li>Exhortation,</li><li>Helps,</li><li>Mercy,</li><li>Service</li></ul></div>
  </section>

  <section class="section" style="top:327px">
    <div class="type-info">
      <h2 class="type-name">EXECUTIVE</h2>
      <p class="type-code">ESTJ-A/ESTJ-T</p>
      <p class="type-desc" style="margin-top:10px">(Excellent administrators, unsurpassed at managing things or people.)</p>
    </div>
    <div class="divider-v" style="height:113px;top:-3px"></div>
    <div class="person c1"><span class="person-name">Marcus Whitaker</span>
      <ul class="gifts"><li>Craftsmanship,</li><li>Exhortation,</li><li>Faith,</li><li>Helps,</li><li>Leadership</li></ul></div>
    <div class="person c2"><span class="person-name">Dale Prescott</span>
      <ul class="gifts"><li>Craftsmanship,</li><li>Giving,</li><li>Healing,</li><li>Miracles,</li><li>Teaching</li></ul></div>
  </section>

  <section class="section" style="top:483px">
    <div class="type-info">
      <h2 class="type-name">ENTREPRENEUR</h2>
      <p class="type-code">ESTP-A/ESTP-T</p>
      <p class="type-desc" style="margin-top:10px">(Smart, energetic and very perceptive people, who truly enjoy living on the edge.)</p>
    </div>
    <div class="divider-v" style="height:113px;top:-5px"></div>
    <div class="person c1"><span class="person-name">Howard Ellis Jr</span>
      <ul class="gifts" style="margin-top:8px"><li>Apostleship,</li><li>Exhortation,</li><li>Faith,</li><li>Giving,</li><li>Teaching</li></ul></div>
    <div class="person c2"><span class="person-name">Rachel Prescott</span>
      <ul class="gifts" style="margin-top:8px"><li>Exhortation,</li><li>Giving,</li><li>Mercy,</li><li>Miracles,</li><li>Prophecy</li></ul></div>
  </section>

  <section class="section" style="top:633px">
    <div class="type-info">
      <h2 class="type-name">ARCHITECT</h2>
      <p class="type-code">INTJ-A/INTJ-T</p>
      <p class="type-desc" style="margin-top:10px">(Imaginative and strategic thinkers, with<br>a plan for everything.)</p>
    </div>
    <div class="divider-v" style="height:113px;top:-2px"></div>
    <div class="person c1"><span class="person-name">Carol Ellis</span>
      <ul class="gifts" style="margin-top:8px"><li>Administration,</li><li>Apostleship,</li><li>Craftsmanship,</li><li>Discernment,</li><li>Helps</li></ul></div>
    <div class="person c2"><span class="person-name">Denise Marlow</span>
      <ul class="gifts" style="margin-top:8px"><li>Administration,</li><li>Discernment,</li><li>Exhortation,</li><li>Prophecy,</li><li>Teaching</li></ul></div>
  </section>

  <section class="section" style="top:783px">
    <div class="type-info">
      <h2 class="type-name">COMMANDER</h2>
      <p class="type-code" style="margin-top:7px">ENTJ-A/ENTJ-T</p>
      <p class="type-desc" style="margin-top:6px">(Bold, imaginative and strong-willed leaders, always finding a way- or making one.)</p>
    </div>
    <div class="divider-v" style="height:236px;top:1px"></div>
    <div class="person c1"><span class="person-name">Gregory Hale</span>
      <ul class="gifts"><li>Administration,</li><li>Apostleship,</li><li>Craftsmanship,</li><li>Discernment,</li><li>Evangelism</li></ul></div>
    <div class="person c2"><span class="person-name">Lydia-Mae Fontaine</span>
      <ul class="gifts"><li>Faith,</li><li>Giving,</li><li>Leadership,</li><li>Miracles,</li><li>Teaching</li></ul></div>
    <div class="person c3"><span class="person-name">Brenda Cole</span>
      <ul class="gifts"><li>Apostleship,</li><li>Craftsmanship,</li><li>Exhortation,</li><li>Faith,</li><li>Giving</li></ul></div>
    <div class="person c4"><span class="person-name">Imani Reyes</span>
      <ul class="gifts"><li>Administration,</li><li>Faith,</li><li>Healing,</li><li>Mercy,</li><li>Teaching</li></ul></div>
    <div class="person c1" style="top:128px"><span class="person-name">Nathan Brockway</span>
      <ul class="gifts" style="margin-top:8px"><li>Administration,</li><li>Discernment,</li><li>Evangelism,</li><li>Pastor/Shepherd,</li><li>Prophecy</li></ul></div>
    <div class="person c2" style="top:128px"><span class="person-name">Paula Grant</span>
      <ul class="gifts" style="margin-top:8px"><li>Evangelism,</li><li>Word of Knowledge,</li><li>Mercy,</li><li>Miracles,</li><li>Teaching</li></ul></div>
    <div class="person c3" style="top:128px"><span class="person-name">Tamira Voss</span>
      <ul class="gifts" style="margin-top:8px"><li>Exhortation,</li><li>Word of Knowledge,</li><li>Admistration,</li><li>Teaching,</li><li>Prophecy</li></ul></div>
  </section>

  <section class="section" style="top:1061px">
    <div class="type-info">
      <h2 class="type-name">PROTAGONIST</h2>
      <p class="type-code">ENFJ-A/ENFJ-T</p>
      <p class="type-desc" style="margin-top:8px">(Charismatic and inspiring leaders, able to mesmerize their listeners.)</p>
    </div>
    <div class="divider-v" style="height:112px;top:-4px"></div>
    <div class="person c1"><span class="person-name">Simon Kessler</span>
      <ul class="gifts" style="margin-top:6px"><li>Apostleship,</li><li>Discernment,</li><li>Evangelism,</li><li>Faith,</li><li>Giving</li></ul></div>
    <div class="person c2"><span class="person-name">Joanna Whitaker</span>
      <ul class="gifts" style="margin-top:6px"><li>Apostleship,</li><li>Discernment,</li><li>Evangelism,</li><li>Faith,</li><li>Words of Wisdom</li></ul></div>
    <div class="person c3" style="left:566px"><span class="person-name">Mabel Dunmore</span>
      <ul class="gifts" style="margin-top:6px"><li>Evangelism</li><li>Exhortation,</li><li>Faith,</li><li>Healing,</li><li>Teaching</li></ul></div>
    <div class="person c4"><span class="person-name">Lonnie Dunmore</span>
      <ul class="gifts" style="margin-top:6px"><li>Craftsmanship,</li><li>Evangelism,</li><li>Faith,</li><li>Healing,</li><li>Teaching</li></ul></div>
  </section>
</div>
</body>
</html>
```